Transformative School Model Needs a Website. I am easy to work with.

Greetings:
I am creating a K-12 school that is a complete and total re-imagination of what education can be for children, families, communities, and the planet. While we will begin as a K-12 school, I really see it as a complete life cycle education (birth to death). I'm looking for a website to describe my new transformational educational model. I anticipate having 7-8 pages. I have all the copy ready.
I am the Founder. I am easy to work with, an effective communicator, and I’m very good at knowing what I want and providing specific and concrete detail, examples, and direction to make sure I use your time wisely.

```html
<!DOCTYPE html>
<html lang="en">
<head>
<meta charset="utf-8">
<title>Bright Meadow Academy</title>
<link href="https://fonts.googleapis.com/css2?family=Fredoka:wght@600;700&family=Montserrat:wght@400;500;600;700&display=swap" rel="stylesheet">
<style>
:root{
  --accent:#f04a2a;
  --ink:#2b2d31;
  --chalk:#2f3236;
  --chalk-deep:#26282c;
  --sky:#b1e0f0;
  --mist:#f0f0f0;
  --rule:#e7e7e7;
  --white:#ffffff;
  --star:#f7b500;
  --head:'Fredoka', 'Arial Rounded MT Bold', sans-serif;
  --body:'Montserrat', Arial, sans-serif;
}
*{box-sizing:border-box;margin:0;padding:0}
html,body{width:1200px;height:3681px;overflow:hidden}
body{font-family:var(--body);color:var(--ink);background:var(--white)}
.page{position:relative;width:1200px;height:3681px;overflow:hidden;
  background:repeating-linear-gradient(to bottom,transparent 0 37px,var(--rule) 37px 38px)}
.abs{position:absolute}
.fill{position:absolute}

/* hero */
.hero{left:0;top:0;width:1200px;height:557px;background:var(--chalk)}
.hero-photo{left:160px;top:90px;width:890px;height:467px;
  background:radial-gradient(ellipse at 50% 60%,#7e6a58 0%,#5a5048 45%,transparent 75%)}
.nav a{position:absolute;top:42px;color:var(--white);font-size:12px;text-decoration:none;font-weight:500}
.brand{position:absolute;display:flex;align-items:center;gap:6px;color:var(--white);font-family:var(--body);font-weight:600}
.brand .dot{width:18px;height:18px;border-radius:50%;background:var(--white);flex:none}
.hero-title{position:absolute;left:0;width:1200px;top:142px;text-align:center;color:var(--white);
  font-family:var(--head);font-weight:700;font-size:50px;letter-spacing:2px}
.zigzag{position:absolute;left:0;width:1200px;height:12px}

/* cards */
.card{position:absolute;width:376px;height:260px;color:var(--white);text-align:center;padding-top:57px}
.card.photo{background:linear-gradient(160deg,#5c564f,#3d3a37 60%,#4a4540)}
.card h3{font-family:var(--head);font-weight:700;font-size:25px;line-height:31px;letter-spacing:1px}
.card .note{font-size:11px;margin-top:10px;line-height:15px;padding:0 28px}
.btn-line{display:inline-block;margin-top:19px;border:1.5px solid var(--white);padding:5px 12px;font-size:11px;font-weight:600;letter-spacing:.3px}
.card.board{background:var(--chalk-deep);text-align:left;padding:28px 46px 0}
.card.board h3{text-align:center;margin-bottom:20px}
.card.board p{font-size:11px;line-height:18px;margin-bottom:12px}

/* split sections */
.btn-solid{position:absolute;background:var(--accent);color:var(--white);font-size:11px;font-weight:600;text-align:center;line-height:27px}
.eyebrow{font-size:11px}
.sec-title{font-family:var(--head);font-weight:700;font-size:27px;letter-spacing:1px;line-height:31px}
.para{font-size:11.5px;line-height:19px}

/* services */
.svc{position:absolute;top:1653px;width:176px;height:191px;background:var(--white);box-shadow:0 2px 10px rgba(0,0,0,.08);padding:24px 0 0 27px}
.svc.on{background:var(--accent);color:var(--white)}
.svc svg{display:block}
.svc h4{font-family:var(--body);font-weight:700;font-size:11.5px;margin-top:32px;letter-spacing:.3px}
.svc p{font-size:11px;line-height:16px;margin-top:12px;width:130px}

/* testimonial */
.quote-band{left:0;top:1897px;width:1200px;height:332px;background:linear-gradient(100deg,#2b2e32,#34373b 50%,#2b2e32);color:var(--white);text-align:center}
.quote-mark{position:absolute;left:112px;top:-30px;font-family:var(--head);font-size:190px;color:#6d7075}

/* news */
.news{position:absolute;top:2319px;width:225px}
.news .pic{height:240px}
.news time{display:block;color:var(--accent);font-size:10px;margin-top:10px;font-weight:500}
.news p{font-size:10px;line-height:16px;margin-top:3px}

/* newsletter */
.field{position:absolute;left:701px;width:286px;height:33px;background:var(--white);font-size:11px;color:#9a9a9a;padding:10px 12px}

/* footer */
.footer{left:0;top:3389px;width:1200px;height:292px;background:var(--ink);color:var(--white)}
.footer h5{position:absolute;top:66px;color:var(--accent);font-size:11.5px;font-weight:700;letter-spacing:.5px}
.footer ul{position:absolute;list-style:none;font-size:11.5px;line-height:25px}
.social{position:absolute;top:195px;width:16px;height:16px;border-radius:50%;background:var(--accent)}
</style>
</head>
<body>
<div class="page">

  <header class="abs hero">
    <div class="fill hero-photo" role="img" aria-label="Photo of five cheering schoolchildren with raised arms in front of a chalkboard"></div>
    <nav class="nav">
      <a href="#" style="left:353px">Home</a>
      <a href="#" style="left:444px">About Us</a>
      <a href="#" style="left:702px">Services</a>
      <a href="#" style="left:808px">Contact</a>
    </nav>
    <div class="brand" style="left:548px;top:40px;font-size:11px"><span class="dot"></span>Bright Meadow</div>
    <h1 class="hero-title">BRIGHT MEADOW ACADEMY</h1>
    <svg class="zigzag" style="top:545px" viewBox="0 0 1200 12" preserveAspectRatio="none">
      <defs><pattern id="zz" width="12" height="12" patternUnits="userSpaceOnUse"><polygon points="0,12 6,2 12,12" fill="#ffffff"/></pattern></defs>
      <rect width="1200" height="12" fill="url(#zz)"/>
    </svg>
  </header>

  <section>
    <article class="card photo" style="left:214px;top:601px" role="img" aria-label="Classroom photo with teacher and students">
      <h3>REQUEST A INTRA<br>DISTRICT OR INCOMING<br>INTER DISTRICT PERMIT</h3>
      <p class="note">April 1 - May 1</p>
      <span class="btn-line">LEARN MORE</span>
    </article>
    <article class="card photo" style="left:609px;top:601px" role="img" aria-label="Photo of young students writing at desks">
      <h3>TRANSITIONAL<br>KINDERGARTEN<br>ENROLLMENT</h3>
      <p class="note">begins February 21, 2023</p>
      <span class="btn-line">LEARN MORE</span>
    </article>
    <article class="card photo" style="left:214px;top:880px;padding-top:55px" role="img" aria-label="Photo of students studying together">
      <h3>MENTAL HEALTH CARE<br>&amp; SUBSTANCE TREATMENT</h3>
      <p class="note">Connect to community-based resources for our students, staff and household members, regardless of insurance status.</p>
      <span class="btn-line" style="margin-top:16px">LEARN MORE</span>
    </article>
    <article class="card board" style="left:609px;top:880px">
      <h3>FRIENDLY REMINDERS</h3>
      <p>2023-2024 Kindergarten Registration</p>
      <p>2022-2023 Annual Parent and Student Rights Notification and Standards of Behavior Handbook</p>
      <p>Apply for Free Before and After School Care</p>
      <p>Online Enrollment Services Available for TK-12 Students</p>
    </article>
  </section>

  <section>
    <div class="fill" style="left:0;top:1191px;width:600px;height:358px;background:var(--sky)"></div>
    <div class="fill" style="left:600px;top:1191px;width:600px;height:358px;background:linear-gradient(120deg,#8a8c90,#c9c2b8 50%,#6f6a66)" role="img" aria-label="Photo of students working with microscopes in a lab"></div>
    <p class="abs eyebrow" style="left:214px;top:1267px">About Us</p>
    <h2 class="abs sec-title" style="left:214px;top:1284px">OUR HISTORY</h2>
    <p class="abs para" style="left:214px;top:1335px;width:290px">Lorem ipsum dolor sit amet, consectetur adipiscing elit, sed do eiusmod tempor incididunt ut labore et dolore magna aliqua. Quis ipsum suspendisse ultrices gravida. Risus commodo viverra maecenas accumsan lacus vel facilisis.</p>
    <a class="btn-solid" style="left:214px;top:1455px;width:129px">LEARN MORE</a>
  </section>

  <section>
    <h2 class="abs sec-title" style="left:0;width:1200px;text-align:center;top:1591px">OUR SERVICES</h2>
    <div class="svc" style="left:226px">
      <svg width="48" height="48" viewBox="0 0 48 48"><circle cx="24" cy="24" r="22" fill="none" stroke="#f04a2a" stroke-width="1.5"/><circle cx="24" cy="24" r="9" fill="none" stroke="#f04a2a" stroke-width="2" stroke-dasharray="4 2"/><circle cx="24" cy="24" r="4" fill="none" stroke="#f04a2a" stroke-width="1.5"/></svg>
      <h4>PROGRAMS</h4><p>Develop fine and gross skills and more</p>
    </div>
    <div class="svc on" style="left:421px">
      <svg width="48" height="48" viewBox="0 0 48 48"><circle cx="24" cy="24" r="22" fill="none" stroke="#fff" stroke-width="1.5"/><rect x="14" y="15" width="20" height="17" fill="none" stroke="#fff" stroke-width="1.6"/><line x1="24" y1="15" x2="24" y2="32" stroke="#fff" stroke-width="1.4"/></svg>
      <h4>ONLINE ED</h4><p>Processes and all main lorem ipsum</p>
    </div>
    <div class="svc" style="left:616px">
      <svg width="48" height="48" viewBox="0 0 48 48"><circle cx="24" cy="24" r="22" fill="none" stroke="#f04a2a" stroke-width="1.5"/><circle cx="24" cy="20" r="8" fill="none" stroke="#f04a2a" stroke-width="1.6"/><polyline points="19,27 17,36 24,32 31,36 29,27" fill="none" stroke="#f04a2a" stroke-width="1.6"/></svg>
      <h4>AWARDS</h4><p>Cycles of<br>time be explored</p>
    </div>
    <div class="svc" style="left:809px">
      <svg width="48" height="48" viewBox="0 0 48 48"><circle cx="24" cy="24" r="22" fill="none" stroke="#f04a2a" stroke-width="1.5"/><circle cx="24" cy="24" r="4" fill="none" stroke="#f04a2a" stroke-width="1.6"/><g stroke="#f04a2a" stroke-width="1.4"><line x1="24" y1="20" x2="24" y2="12"/><line x1="24" y1="28" x2="24" y2="36"/><line x1="20" y1="24" x2="12" y2="24"/><line x1="28" y1="24" x2="36" y2="24"/></g><g fill="#f04a2a"><circle cx="24" cy="11" r="2.5"/><circle cx="24" cy="37" r="2.5"/><circle cx="11" cy="24" r="2.5"/><circle cx="37" cy="24" r="2.5"/></g></svg>
      <h4>COMMUNITY</h4><p>Built co-<br>mmunity to learn.</p>
    </div>
  </section>

  <section class="abs quote-band" role="img" aria-label="Chalkboard covered with handwritten math formulas">
    <span class="quote-mark">“</span>
    <h2 class="abs sec-title" style="left:0;width:1200px;top:39px;font-size:25px">TESTIMONIAL</h2>
    <p class="abs" style="left:210px;width:780px;top:101px;font-size:17.5px;line-height:25px">Lorem ipsum dolor sit amet, consectetur adipiscing elit, sed do eiusmod tempor incididunt ut labore et dolore magna aliqua. Quis ipsum suspendisse ultrices gravida. Risus commodo viverra maecenas accumsan lacus vel facilisis.”</p>
    <svg class="abs" style="left:543px;top:197px" width="114" height="18" viewBox="0 0 114 18">
      <defs><polygon id="st" points="9,0 11.6,6 18,6.5 13,10.7 14.6,17 9,13.6 3.4,17 5,10.7 0,6.5 6.4,6"/></defs>
      <g fill="#f7b500"><use href="#st" x="0"/><use href="#st" x="24"/><use href="#st" x="48"/><use href="#st" x="72"/><use href="#st" x="96"/></g>
    </svg>
    <a class="btn-solid" style="left:536px;top:246px;width:128px">LEARN MORE</a>
  </section>

  <section>
    <h2 class="abs sec-title" style="left:0;width:1200px;text-align:center;top:2254px">LATEST NEWS</h2>
    <article class="news" style="left:214px">
      <div class="pic" style="background:linear-gradient(150deg,#c9c4bb,#8d6d5a 60%,#5a4c44)" role="img" aria-label="Photo of a student raising her hand in class"></div>
      <time>19 Feb, 2023</time>
      <p>Lorem ipsum dolor sit amet, consectetur adipiscing elit, sed do eiusmod tempor incididunt ut labore et dolore magna aliqua.</p>
    </article>
    <article class="news" style="left:483px">
      <div class="pic" style="background:linear-gradient(150deg,#d8d3cc,#8a8f96 55%,#4b6e9a)" role="img" aria-label="Photo of students giving a high five"></div>
      <time>02 Jan, 2023</time>
      <p>Lorem ipsum dolor sit amet, consectetur adipiscing elit, sed do eiusmod tempor incididunt ut labore et dolore magna aliqua.</p>
    </article>
    <article class="news" style="left:750px">
      <div class="pic" style="background:linear-gradient(150deg,#4f5f52,#6b5f55 55%,#2c2c2e)" role="img" aria-label="Photo of two students talking in front of a chalkboard"></div>
      <time>23 Dec, 2022</time>
      <p>Lorem ipsum dolor sit amet, consectetur adipiscing elit, sed do eiusmod tempor incididunt ut labore et dolore magna aliqua.</p>
    </article>
  </section>

  <section>
    <div class="fill" style="left:0;top:2689px;width:600px;height:357px;background:var(--mist)"></div>
    <div class="fill" style="left:600px;top:2689px;width:600px;height:357px;background:linear-gradient(120deg,#4a5a3e,#2a2a30 50%,#6a6a60)" role="img" aria-label="Photo of smiling graduates in caps and gowns holding diplomas"></div>
    <h2 class="abs sec-title" style="left:214px;top:2747px">EQUITY &amp; DIVERSITY<br>STATEMENT</h2>
    <p class="abs para" style="left:214px;top:2830px;width:300px">BMA has always celebrated differences and was founded on the principles of shedding labels and breaking down artificial barriers. At our core, we are dedicated to building and sustaining equity by actively embracing diversity in our community.</p>
    <a class="btn-solid" style="left:214px;top:2950px;width:129px">LEARN MORE</a>
  </section>

  <section>
    <div class="fill" style="left:0;top:3046px;width:600px;height:343px;background:linear-gradient(120deg,#cfd6dc,#efece6 45%,#9aa0a6)" role="img" aria-label="Photo of students in lab coats using microscopes"></div>
    <div class="fill" style="left:600px;top:3046px;width:600px;height:343px;background:var(--sky)"></div>
    <h2 class="abs sec-title" style="left:703px;top:3118px">SUBSCRIBE OUR<br>NEWSLETTER</h2>
    <div class="field" style="top:3196px">Name</div>
    <div class="field" style="top:3240px">Email</div>
    <a class="btn-solid" style="left:703px;top:3297px;width:130px">SUBSCRIBE</a>
  </section>

  <footer class="abs footer">
    <svg class="zigzag" style="top:-12px" viewBox="0 0 1200 12" preserveAspectRatio="none">
      <defs><pattern id="zz2" width="12" height="12" patternUnits="userSpaceOnUse"><polygon points="0,12 6,2 12,12" fill="#2b2d31"/></pattern></defs>
      <rect width="1200" height="12" fill="url(#zz2)"/>
    </svg>
    <div class="brand" style="left:214px;top:70px;font-size:12px"><span class="dot" style="width:30px;height:30px"></span>Bright Meadow</div>
    <p class="abs" style="left:214px;top:142px;font-size:11.5px;line-height:16px">© 2023 BRIGHT MEADOW<br>ACADEMY. All rights reserved.</p>
    <span class="social" style="left:214px"></span>
    <span class="social" style="left:252px"></span>
    <span class="social" style="left:292px"></span>

    <h5 style="left:484px">ABOUT</h5>
    <ul style="left:484px;top:100px"><li>Lorem ipsum dolor sit</li><li>amet, consectetur</li><li>adipiscing elit, sed do</li><li>eiusmod tempor</li></ul>

    <h5 style="left:731px">QUICK LINK</h5>
    <ul style="left:731px;top:98px"><li>Home</li><li>About Us</li><li>Services</li><li>Testimonials</li><li>Contact</li></ul>

    <h5 style="left:923px">FOLLOW US</h5>
    <ul style="left:923px;top:98px"><li>Chatterbox</li><li>Snapgrid</li><li>Tweetline</li></ul>
  </footer>

</div>
</body>
</html>
```